Web page design for technology solution company
Velmork Inc.
Dear PH,
Kindly star rate #83 it will help me to go through.
Thanks!
Hi PH,
Any feedback for #52
Thanks
Kindly check your private messages.
#57 and #58 - don't need the extra info. Stick with your earlier versions - like those better. They're simple and not 'overloaded'
#55, #56 - like the simplicity but don't like the dark background
Hi PH, please check your private message. thanks
#13 and #19 - can we see the design without the graphics?
#20 -#24 - much better with the lighter background!
@PH
Kindly check your private message box on the top right & reply asap with your feedback.Thanks
#10 - #12. They seem interesting but on the darker side. Can we see them with a white background?
#9 - Nice and clean design. It's unique and colors are nicely coordinated. Can you find a place for social media icons?
#1 - #5 . Some of the designs look interesting but the background is too dark. Can we see the same with white background?
PH please check your private message
Perin Koldesh

```html
<!DOCTYPE html>
<html lang="en">
<head>
<meta charset="utf-8">
<title>Velmork Inc.</title>
<link rel="stylesheet" href="https://fonts.googleapis.com/css2?family=Open+Sans:wght@400;600&family=Oswald:wght@400&display=swap">
<style>
  :root {
    --page-light: #f7f7f7;
    --page-mid: #e4e4e4;
    --page-shade: #cfcfcf;
    --band-top: #dcdcdc;
    --band-bottom: #ebebeb;
    --accent-green: #8fb02a;
    --accent-green-dark: #7a9922;
    --ink-dark: #2f2f2f;
    --ink-mid: #4a4a4a;
    --ink-soft: #8a8a8a;
    --icon-dark: #4b4b4b;
    --icon-light: #8c8c8c;
    --white: #ffffff;
  }
  * { margin: 0; padding: 0; box-sizing: border-box; }
  html, body { width: 1200px; height: 588px; overflow: hidden; }
  body {
    position: relative;
    font-family: "Open Sans", Arial, sans-serif;
    background:
      radial-gradient(ellipse 70% 60% at 50% 0%, var(--white) 0%, rgba(255,255,255,0) 70%),
      linear-gradient(180deg, var(--page-light) 0%, var(--page-mid) 60%, var(--page-shade) 100%);
  }
  .brand {
    position: absolute; top: 44px; left: 0; width: 1200px;
    display: flex; justify-content: center; align-items: center; gap: 14px;
  }
  .brand-mark {
    width: 46px; height: 46px; border-radius: 50%;
    background: var(--accent-green);
  }
  .brand-name {
    font-family: "Oswald", "Arial Narrow", sans-serif;
    font-size: 56px; font-weight: 400; color: var(--ink-mid);
    letter-spacing: 1px; line-height: 1;
  }
  .nav-band {
    position: absolute; left: 0; top: 138px; width: 1200px; height: 214px;
    background:
      linear-gradient(90deg, rgba(255,255,255,0) 0%, rgba(255,255,255,0.55) 50%, rgba(255,255,255,0) 100%),
      linear-gradient(180deg, var(--band-top) 0%, var(--band-bottom) 100%);
    border-top: 1px solid rgba(255,255,255,0.8);
    border-bottom: 1px solid rgba(255,255,255,0.8);
  }
  .nav {
    position: absolute; top: 156px; left: 264px;
    display: flex; list-style: none;
  }
  .nav-item {
    width: 192px; height: 209px; margin-right: 10px;
    display: flex; flex-direction: column; align-items: center;
    padding-top: 44px;
  }
  .nav-item.is-active { background: var(--accent-green); }
  .nav-icon {
    width: 96px; height: 96px; border-radius: 14px;
  }
  .icon-person { background: radial-gradient(circle at 50% 35%, #6a6a6a, #1f1f1f); border-radius: 48px 48px 14px 14px; }
  .icon-folder { background: linear-gradient(180deg, var(--icon-light), var(--icon-dark)); }
  .icon-chat { background: linear-gradient(180deg, #9a9a9a, #555555); border-radius: 40px; }
  .nav-label {
    margin-top: 16px;
    font-family: "Oswald", "Arial Narrow", sans-serif;
    font-size: 22px; letter-spacing: 0.5px; color: var(--ink-dark);
  }
  .nav-item.is-active .nav-label { color: var(--white); }
  .tagline {
    position: absolute; top: 414px; left: 0; width: 1200px; text-align: center;
  }
  .tagline-main { font-size: 24px; color: var(--ink-dark); }
  .tagline-sub { margin-top: 2px; font-size: 13.5px; color: var(--ink-mid); }
  .footer {
    position: absolute; left: 0; top: 532px; width: 1200px; height: 56px;
    background: linear-gradient(180deg, rgba(255,255,255,0.5), rgba(200,200,200,0.4));
    border-top: 1px solid rgba(255,255,255,0.9);
  }
  .footer-brand {
    position: absolute; left: 204px; top: 14px;
    display: flex; align-items: center; gap: 6px;
  }
  .footer-brand .brand-mark { width: 16px; height: 16px; background: var(--ink-soft); }
  .footer-brand .brand-name { font-size: 20px; color: var(--ink-soft); }
  .copyright {
    position: absolute; left: 0; width: 1200px; top: 21px;
    text-align: center; font-size: 11px; color: var(--ink-soft);
  }
  .social {
    position: absolute; left: 899px; top: 12px; display: flex; gap: 10px; list-style: none;
  }
  .social-dot {
    width: 30px; height: 30px; border-radius: 50%;
    background: linear-gradient(180deg, #b0b0b0, #8e8e8e);
  }
</style>
</head>
<body>
  <header class="brand">
    <span class="brand-mark"></span>
    <span class="brand-name">Velmork Inc.</span>
  </header>

  <div class="nav-band"></div>
  <ul class="nav">
    <li class="nav-item is-active">
      <div class="nav-icon icon-person" role="img" aria-label="Grey glossy silhouette of a person"></div>
      <span class="nav-label">ABOUT US</span>
    </li>
    <li class="nav-item">
      <div class="nav-icon icon-folder" role="img" aria-label="Dark folder with a mobile phone symbol"></div>
      <span class="nav-label">PRODUCTS</span>
    </li>
    <li class="nav-item">
      <div class="nav-icon icon-chat" role="img" aria-label="Two overlapping grey speech bubbles"></div>
      <span class="nav-label">CONTACT</span>
    </li>
  </ul>

  <section class="tagline">
    <p class="tagline-main">We provide branded online and mobile platforms and service solutions</p>
    <p class="tagline-sub">that enable and enhance eCommerce and other online interactions for individuals and businesses.</p>
  </section>

  <footer class="footer">
    <div class="footer-brand">
      <span class="brand-mark"></span>
      <span class="brand-name">Velmork Inc.</span>
    </div>
    <p class="copyright">Copyright © 2012 Velmork Inc. All Rights Reserved</p>
    <ul class="social" aria-label="Social links">
      <li class="social-dot"></li>
      <li class="social-dot"></li>
      <li class="social-dot"></li>
    </ul>
  </footer>
</body>
</html>
```